Verpackungen für Nahrungsergänzungsmittel
Zielgruppe
Wir vertreiben Nahrungsergänzungsmittel über Apotheken sowie E-commerce Plattformen wie Quorvex.
Aufgabenstellung
Die Verpackungen (Faltschachteln) werden für eine neue Produktlinie (Nahrungsergänzungsmittelserie) benötigt. Also Beispielsweise wird es 3 Produkte geben (Vitamin C, Zink und Eisen). Die genannten Produkte sind lediglich Beispiele. Wichtig bei dem Produktdesign ist, dass ein Element (zum Beispiel) oder ähnliches in jeder Verpackung vorkommt, so dass es einen Wiedererkennungswert für die Marke gibt.
Ein Logo, gesetzliche Pflichtangaben oder Werbetexte spielen erstmal keine Rolle. Es geht in einem ersten Schritt nur darum 'Grunddesigns' zu erstellen. Auch besondere/gewünschte Farben gibt es keine. Es muss einfach nur schön aussehen :-)
Bei Fragen gerne melden..
Ps: Ein Beispielsstanze einer Faltschachtel ist angehängt.

```html
<!DOCTYPE html>
<html lang="de">
<head>
<meta charset="utf-8">
<title>VELTA – Verpackungsserie Nahrungsergänzungsmittel</title>
<link rel="stylesheet" href="https://fonts.googleapis.com/css2?family=Montserrat:wght@600;700&family=Open+Sans:wght@400;600;700&family=Playfair+Display:wght@700;800&family=Roboto+Condensed:wght@400&display=swap">
<style>
  :root {
    --page-bg: #eef0f3;
    --paper: #f7f7f8;
    --ink: #4a4a4c;
    --ink-soft: #6d6d70;
    --rule: #8a8a8e;

    --orange-light: #f3a637;
    --orange-dark: #e2612a;
    --blue-light: #4a9fe3;
    --blue-dark: #1b4f8f;
    --blue-deep: #243a5a;
    --purple-light: #b45aa8;
    --purple-dark: #4a2450;
  }

  * { box-sizing: border-box; margin: 0; padding: 0; }

  html, body {
    width: 1200px;
    height: 800px;
    overflow: hidden;
    background: var(--page-bg);
    font-family: "Open Sans", sans-serif;
    color: var(--ink);
  }

  .product-line {
    position: relative;
    width: 1200px;
    height: 800px;
    display: flex;
    justify-content: center;
    align-items: center;
    gap: 40px;
  }

  .carton {
    position: relative;
    width: 340px;
    height: 480px;
    background: var(--paper);
    box-shadow: 0 14px 30px rgba(40, 50, 70, 0.16);
    overflow: hidden;
  }

  .carton--vitamin-c { --tone-a: var(--orange-light); --tone-b: var(--orange-dark); --accent: var(--orange-dark); }
  .carton--zinc      { --tone-a: var(--blue-dark);    --tone-b: var(--blue-light);  --accent: #2f78c8; }
  .carton--iron      { --tone-a: var(--purple-light); --tone-b: var(--purple-dark); --accent: #6b2f73; }

  /* coloured head panel */
  .carton__head {
    position: absolute;
    left: 0; top: 0;
    width: 100%;
    height: 192px;
    background: linear-gradient(115deg, var(--tone-a), var(--tone-b));
  }

  .brand {
    position: absolute;
    left: 34px; top: 52px;
    display: flex;
    align-items: center;
    gap: 8px;
    font-family: "Montserrat", sans-serif;
    font-weight: 700;
    font-size: 40px;
    letter-spacing: 1px;
    color: #ffffff;
  }
  .brand__dot {
    width: 12px; height: 12px;
    border-radius: 50%;
    background: #ffffff;
  }

  .claim {
    position: absolute;
    left: 40px; top: 150px;
    padding: 3px 10px;
    font-family: "Roboto Condensed", sans-serif;
    font-size: 14px;
    color: #ffffff;
    border-left: 1px solid rgba(255,255,255,0.85);
    border-right: 1px solid rgba(255,255,255,0.85);
  }
  .claim::before, .claim::after {
    content: "";
    position: absolute;
    width: 8px; height: 100%;
    top: 0;
    border-top: 1px solid rgba(255,255,255,0.85);
    border-bottom: 1px solid rgba(255,255,255,0.85);
  }
  .claim::before { left: 0; }
  .claim::after { right: 0; }

  .element-art {
    position: absolute;
    right: 22px; top: 20px;
    width: 70px; height: 160px;
    border-radius: 35px;
    background: linear-gradient(180deg, rgba(255,255,255,0.32), rgba(255,255,255,0.08));
  }

  /* white body panel */
  .bubble-art {
    position: absolute;
    left: 6px; top: 208px;
    width: 60px; height: 230px;
    border-radius: 30px;
    background: radial-gradient(ellipse at center, rgba(150, 195, 230, 0.35), rgba(150, 195, 230, 0));
  }

  .tagline {
    position: absolute;
    left: 0; top: 222px;
    width: 300px;
    padding-right: 12px;
    padding-bottom: 5px;
    text-align: right;
    font-family: "Roboto Condensed", sans-serif;
    font-size: 12.5px;
    letter-spacing: 0.5px;
    color: var(--ink-soft);
    border-bottom: 1px solid var(--rule);
  }
  .tagline::after {
    content: "";
    position: absolute;
    right: 0; bottom: -6px;
    width: 2px; height: 22px;
    background: var(--accent);
  }

  .product-name {
    position: absolute;
    left: 38px; top: 256px;
    display: flex;
    align-items: flex-end;
    gap: 8px;
    font-family: "Playfair Display", serif;
    line-height: 1;
  }
  .product-name__word {
    font-weight: 800;
    font-size: 40px;
    letter-spacing: 0.5px;
    color: #58585a;
  }
  .product-name__stack {
    display: flex;
    flex-direction: column;
    align-items: flex-end;
  }
  .product-name__sub {
    font-weight: 700;
    font-size: 20px;
    letter-spacing: 1px;
    color: var(--accent);
    margin-top: 2px;
  }
  .product-name__symbol {
    font-weight: 800;
    font-size: 60px;
    color: var(--accent);
  }

  .facts {
    position: absolute;
    left: 116px; top: 340px;
    display: flex;
    border-radius: 6px;
    background: linear-gradient(90deg, var(--tone-a), var(--tone-b));
    color: #ffffff;
    padding: 4px 6px;
  }
  .carton--zinc .facts { background: linear-gradient(90deg, #3b6a9a, var(--blue-deep)); }
  .facts__item {
    padding: 0 6px;
    text-align: center;
    line-height: 1;
  }
  .facts__item + .facts__item { border-left: 1px solid rgba(255,255,255,0.8); }
  .facts__value { font-weight: 600; font-size: 15px; }
  .facts__value small { font-size: 8px; }
  .facts__label { display: block; font-size: 6.5px; margin-top: 2px; }

  .object-art {
    position: absolute;
    right: 14px; top: 340px;
    width: 90px; height: 96px;
    border-radius: 45px;
  }
  .carton--vitamin-c .object-art { background: radial-gradient(circle, rgba(245,160,40,0.7), rgba(245,160,40,0)); }
  .carton--zinc .object-art { left: 40px; right: auto; top: 380px; width: 70px; height: 50px; background: radial-gradient(circle, rgba(220,226,232,1), rgba(220,226,232,0)); }
  .carton--zinc .object-art--second { left: auto; right: 18px; top: 390px; width: 70px; height: 70px; background: radial-gradient(circle, rgba(200,225,245,1), rgba(200,225,245,0)); }
  .carton--iron .object-art { right: 6px; top: 335px; width: 110px; height: 105px; border-radius: 52px; background: radial-gradient(circle, rgba(70,130,215,0.8), rgba(70,130,215,0)); }

  .supplement-note {
    position: absolute;
    left: 116px; top: 385px;
    width: 120px;
    padding: 5px 6px;
    text-align: center;
    font-size: 7.5px;
    line-height: 1.25;
    color: var(--ink);
    border-left: 1px solid #b7b7ba;
    border-right: 1px solid #b7b7ba;
  }
  .supplement-note::before, .supplement-note::after {
    content: "";
    position: absolute;
    top: 0; width: 6px; height: 100%;
    border-top: 1px solid #b7b7ba;
    border-bottom: 1px solid #b7b7ba;
  }
  .supplement-note::before { left: 0; }
  .supplement-note::after { right: 0; }

  .net-weight {
    position: absolute;
    left: 0; top: 440px;
    width: 100%;
    text-align: center;
    font-family: "Roboto Condensed", sans-serif;
    font-size: 7px;
    color: var(--ink-soft);
  }

  .carton__foot {
    position: absolute;
    left: 0; bottom: 0;
    width: 100%;
    height: 18px;
  }
  .carton--vitamin-c .carton__foot { background: linear-gradient(90deg, var(--orange-dark), var(--orange-light)); }
  .carton--zinc .carton__foot { background: linear-gradient(90deg, var(--blue-deep), #4f7fb0, var(--blue-deep)); }
  .carton--iron .carton__foot { background: linear-gradient(90deg, var(--purple-light), var(--purple-dark)); }
</style>
</head>
<body>
<main class="product-line">

  <!-- Vitamin C -->
  <section class="carton carton--vitamin-c">
    <div class="carton__head">
      <div class="brand"><span>VELTA</span><span class="brand__dot"></span></div>
      <div class="element-art" role="img" aria-label="Aufsteigende Blasen mit dem Elementsymbol C"></div>
      <div class="claim">100 % NATÜRLICH</div>
    </div>

    <div class="bubble-art" role="img" aria-label="Aufsteigende Wasserblasen"></div>
    <div class="tagline">IMMUNSYSTE &amp; ZELLSCHUTZ</div>
    <h2 class="product-name">
      <span class="product-name__word">VITAMIN</span>
      <span class="product-name__symbol">C</span>
    </h2>
    <div class="object-art" role="img" aria-label="Geöffnete orange Kapsel mit Pulver"></div>
    <div class="facts">
      <div class="facts__item"><span class="facts__value">12<small>g</small></span><span class="facts__label">Protein</span></div>
      <div class="facts__item"><span class="facts__value">250</span><span class="facts__label">Calories</span></div>
      <div class="facts__item"><span class="facts__value">26</span><span class="facts__label">Vitamins &amp;<br>Minerals</span></div>
    </div>
    <p class="supplement-note">Nahrungsergänzungsmittel<br>zur Versorgung mit<br>Vitamin C</p>
    <p class="net-weight">NET WT. 14 OZ (397 g)</p>
    <div class="carton__foot"></div>
  </section>

  <!-- Zink -->
  <section class="carton carton--zinc">
    <div class="carton__head">
      <div class="brand"><span>VELTA</span><span class="brand__dot"></span></div>
      <div class="element-art" role="img" aria-label="Aufsteigende Blasen mit dem Elementsymbol Zn"></div>
      <div class="claim">100 % NATÜRLICH</div>
    </div>

    <div class="bubble-art" role="img" aria-label="Aufsteigende Wasserblasen"></div>
    <div class="tagline">IMMUNSYSTE &amp; ZELLSCHUTZ</div>
    <h2 class="product-name">
      <span class="product-name__stack">
        <span class="product-name__word">VITAMIN</span>
        <span class="product-name__sub">ZINK</span>
      </span>
      <span class="product-name__symbol">Zn</span>
    </h2>
    <div class="object-art" role="img" aria-label="Weiße Tabletten"></div>
    <div class="object-art object-art--second" role="img" aria-label="Sprudelnde Brausetablette"></div>
    <div class="facts">
      <div class="facts__item"><span class="facts__value">12<small>g</small></span><span class="facts__label">Protein</span></div>
      <div class="facts__item"><span class="facts__value">250</span><span class="facts__label">Calories</span></div>
      <div class="facts__item"><span class="facts__value">26</span><span class="facts__label">Vitamins &amp;<br>Minerals</span></div>
    </div>
    <p class="supplement-note">Nahrungsergänzungsmittel<br>zur Versorgung mit<br>Vitamin C</p>
    <p class="net-weight">NET WT. 14 OZ (397 g)</p>
    <div class="carton__foot"></div>
  </section>

  <!-- Eisen -->
  <section class="carton carton--iron">
    <div class="carton__head">
      <div class="brand"><span>VELTA</span><span class="brand__dot"></span></div>
      <div class="element-art" role="img" aria-label="Aufsteigende Blasen mit dem Elementsymbol FE"></div>
      <div class="claim">100 % NATÜRLICH</div>
    </div>

    <div class="bubble-art" role="img" aria-label="Aufsteigende Wasserblasen"></div>
    <div class="tagline">IMMUNSYSTE &amp; ZELLSCHUTZ</div>
    <h2 class="product-name">
      <span class="product-name__stack">
        <span class="product-name__word">VITAMIN</span>
        <span class="product-name__sub">EISEN</span>
      </span>
      <span class="product-name__symbol">FE</span>
    </h2>
    <div class="object-art" role="img" aria-label="Explodierende blaue Pulverwolke"></div>
    <div class="facts">
      <div class="facts__item"><span class="facts__value">12<small>g</small></span><span class="facts__label">Protein</span></div>
      <div class="facts__item"><span class="facts__value">250</span><span class="facts__label">Calories</span></div>
      <div class="facts__item"><span class="facts__value">26</span><span class="facts__label">Vitamins &amp;<br>Minerals</span></div>
    </div>
    <p class="supplement-note">Nahrungsergänzungsmittel<br>zur Versorgung mit<br>Vitamin C</p>
    <p class="net-weight">NET WT. 14 OZ (397 g)</p>
    <div class="carton__foot"></div>
  </section>

</main>
</body>
</html>
```